Simple Wordpress "Coming soon" style website (1-3 sections) for a new games company.

This should be a relatively simple, but high-quality website, as it's only intended to be a placeholder for a later more complete website. 42K17T SEZC is a newly-established multi-platform games development company based in the Caribbean. We have a company logo. The logo is only three-colour and uses the Adobe Trajan font. Our business cards also use Adobe Georgia font for email/web addresses and phone numbers, as the Trajan font is capitals only. Our tagline is "Where Games Are Reimagined". Our first app, "Lumo", is in the final stages of development but it's not ready, so we need a "coming soon" style landing (splash) page, with "About Us", "Contact Us" and "Product Timeline" details. We have a Lumo product logo that can be included with the details, plus a screenshot of an in-progress game. The site design needs to allow for multilingual content. It doesn't require a translation plugin, as we've provided the "About Us" and "Product Timeline" content in 16 languages. The only contact details will be the email address. Examples of similar products / companies (if that helps) are "Shade By Tile / Brindlewood", "Merry Hue / Q-Drift", and "Block Craft / SwiftMind". Please note that, with reference to the final selected design, we will need the ability to edit the content, as friends in all 15 countries will be supplying us with colloquially edited versions of the welcome blurb, and we can quickly supply replacement photographic imagery for any backgrounds or POS material. Please ask if you need any further information.
Target Market(s)
18-44yo puzzle gamers (40% male - 60% female)
Industry/Entity Type
Computer games industry
Coding
Coded - Design and coding required
Number of Pages Required
1 page
Font styles to use
Look and feel

```html
<!DOCTYPE html>
<html lang="en">
<head>
<meta charset="utf-8">
<title>42K17T SEZC — Where Games Are Reimagined</title>
<link rel="stylesheet" href="https://fonts.googleapis.com/css2?family=Cinzel:wght@400;600;700&family=Montserrat:wght@400;500;600&display=swap">
<style>
  :root {
    --navy: #0b2a4a;
    --deep: #0a1f38;
    --ocean: #15618a;
    --teal: #1c8f9e;
    --jade: #2a9d6c;
    --leaf: #3fae5a;
    --sky: #2b86c6;
    --white: #ffffff;
    --ink: #2b3a48;
    --muted: #7d8b96;
    --line: #b9c3cb;
    --title: #1f8fa0;
  }
  * { box-sizing: border-box; margin: 0; padding: 0; }
  html, body { width: 1200px; height: 2796px; overflow: hidden; }
  body {
    position: relative;
    background: var(--white);
    font-family: "Montserrat", Arial, sans-serif;
    color: var(--ink);
  }
  .serif { font-family: "Cinzel", "Times New Roman", serif; }

  /* ---------- Hero ---------- */
  .hero {
    position: absolute; left: 0; top: 0; width: 1200px; height: 620px;
    clip-path: polygon(0 0, 100% 0, 100% 80%, 50% 100%, 0 80%);
  }
  .hero-art {
    position: absolute; inset: 0;
    background:
      radial-gradient(ellipse 380px 260px at 22% 78%, rgba(80,200,150,.55), transparent 70%),
      radial-gradient(ellipse 420px 240px at 82% 70%, rgba(40,170,190,.45), transparent 70%),
      radial-gradient(ellipse 500px 200px at 50% 20%, rgba(120,200,240,.35), transparent 70%),
      linear-gradient(180deg, #123e66 0%, #1a6a8c 45%, #1f8a86 75%, #1f6e5e 100%);
  }
  .topbar {
    position: absolute; right: 0; top: 0; width: 620px; height: 44px;
    background: rgba(6,24,44,.75);
    display: flex; align-items: center; justify-content: flex-end; gap: 22px;
    padding-right: 28px; font-size: 13px; color: var(--white);
  }
  .topbar span { display: flex; align-items: center; gap: 6px; }
  .brand {
    position: absolute; left: 70px; top: 38px;
    display: flex; align-items: center; gap: 12px;
  }
  .brand-dot { width: 22px; height: 22px; border-radius: 50%; background: var(--white); }
  .brand-name { font-family: "Cinzel", serif; font-weight: 600; font-size: 34px; color: var(--white); letter-spacing: 1px; }
  .nav {
    position: absolute; left: 440px; top: 60px; height: 36px;
    display: flex; align-items: center; gap: 0;
    font-family: "Cinzel", serif; font-size: 17px; color: var(--white); letter-spacing: 1px;
  }
  .nav a { color: inherit; text-decoration: none; padding: 0 26px; border-right: 1px solid rgba(255,255,255,.6); }
  .nav a:last-of-type { border-right: 0; }
  .lang {
    margin-left: 14px; border: 1px solid rgba(255,255,255,.8); padding: 4px 10px;
    font-family: "Montserrat", sans-serif; font-size: 13px; display: flex; gap: 8px; align-items: center;
  }
  .hero-title {
    position: absolute; left: 0; width: 1200px; top: 158px; text-align: center; color: var(--white);
    font-family: "Cinzel", serif;
  }
  .hero-title h1 { font-size: 104px; font-weight: 700; line-height: 1; letter-spacing: 4px; }
  .hero-title .sezc {
    display: inline-block; margin-top: 8px; padding: 2px 18px;
    border-top: 2px solid var(--white); border-bottom: 2px solid var(--white);
    font-size: 26px; font-weight: 600; letter-spacing: 4px;
  }
  .hero-title .tagline { margin-top: 14px; font-size: 50px; font-weight: 600; letter-spacing: 3px; }

  /* ---------- About ---------- */
  .about {
    position: absolute; left: 220px; top: 720px; width: 760px; height: 570px;
    background: linear-gradient(135deg, #0c2d52 0%, #124a74 55%, #1a7785 100%);
    color: var(--white); text-align: center; padding: 56px 70px 0;
  }
  .about h2 { font-family: "Cinzel", serif; font-size: 58px; font-weight: 700; letter-spacing: 3px; margin-bottom: 26px; }
  .about p { font-size: 18px; line-height: 1.6; margin-bottom: 22px; }

  .product-badge {
    position: absolute; left: 532px; top: 1234px; width: 136px; height: 136px; border-radius: 50%;
    background: var(--white); padding: 8px;
    box-shadow: 0 6px 18px rgba(0,0,0,.2);
  }
  .product-badge div {
    width: 100%; height: 100%; border-radius: 50%;
    background: linear-gradient(135deg, var(--leaf), var(--teal));
    display: flex; align-items: center; justify-content: center;
    font-family: "Cinzel", serif; font-weight: 700; font-size: 34px; color: var(--white);
  }

  /* ---------- Timeline ---------- */
  .timeline-title {
    position: absolute; left: 0; width: 1200px; top: 1450px; text-align: center;
    font-family: "Cinzel", serif; font-weight: 700; font-size: 64px; color: var(--title); letter-spacing: 4px;
  }
  .timeline-line { position: absolute; left: 0; top: 1660px; width: 1200px; height: 3px; background: var(--line); }
  .milestone { position: absolute; width: 200px; margin-left: -100px; text-align: center; }
  .milestone .dot {
    position: absolute; left: 58px; top: 1620px; width: 84px; height: 84px; border-radius: 50%;
    border: 5px solid var(--white); box-shadow: 0 0 0 2px var(--line);
    display: flex; align-items: center; justify-content: center;
    color: var(--white); font-size: 18px; font-weight: 600;
  }
  .dot.blue { background: var(--sky); }
  .dot.green { background: var(--jade); }
  .milestone .label {
    position: absolute; left: 0; width: 200px;
    font-family: "Cinzel", serif; font-weight: 700; font-size: 19px; line-height: 1.25; color: var(--ink);
  }
  .label.above { top: 1540px; height: 66px; display: flex; align-items: flex-end; justify-content: center; }
  .label.below { top: 1718px; }
  .tick { position: absolute; left: 99px; width: 2px; background: var(--line); }

  /* ---------- Game screen ---------- */
  .device {
    position: absolute; left: 192px; top: 1860px; width: 860px; height: 510px; z-index: 2;
    background: #1b1d22; border-radius: 40px; padding: 22px 26px;
    box-shadow: 0 10px 30px rgba(0,0,0,.35);
  }
  .device .screen {
    width: 100%; height: 100%; border-radius: 20px;
    background:
      radial-gradient(circle 120px at 42% 50%, #c9b9d8, transparent 75%),
      linear-gradient(90deg, #e9e3d8 0 8%, #d8d2c6 8% 86%, #5d4a3a 86% 100%);
  }

  /* ---------- Contact ---------- */
  .contact {
    position: absolute; left: 0; top: 2150px; width: 1200px; height: 612px;
    background:
      radial-gradient(ellipse 500px 260px at 50% 35%, rgba(90,200,200,.35), transparent 70%),
      radial-gradient(ellipse 400px 300px at 12% 30%, rgba(40,130,80,.6), transparent 70%),
      radial-gradient(ellipse 400px 300px at 90% 40%, rgba(30,130,90,.55), transparent 70%),
      linear-gradient(180deg, #17564a 0%, #154c6a 50%, #0c2b4c 100%);
    color: var(--white); text-align: center;
  }
  .contact h2 { position: absolute; left: 0; width: 100%; top: 240px; font-family: "Cinzel", serif; font-size: 66px; font-weight: 700; letter-spacing: 3px; }
  .contact .by { position: absolute; left: 0; width: 100%; top: 320px; font-size: 38px; font-weight: 500; }
  .contact .by strong { font-weight: 600; }
  .btn {
    position: absolute; left: 520px; top: 396px; width: 160px; height: 44px;
    border: 1.5px solid var(--white); border-radius: 22px;
    display: flex; align-items: center; justify-content: center; gap: 8px;
    font-size: 14px; font-weight: 600; letter-spacing: 1px; color: var(--white);
  }
  .footer {
    position: absolute; left: 0; top: 2762px; width: 1200px; height: 34px;
    display: flex; align-items: center; justify-content: center;
    font-size: 13px; color: var(--muted); background: var(--white);
  }
</style>
</head>
<body>

<header class="hero">
  <div class="hero-art" role="img" aria-label="Fantasy island landscape at dusk with palm trees, cliffs and glowing sea"></div>
  <div class="topbar">
    <span>
      <svg width="12" height="14" viewBox="0 0 12 14"><path d="M6 0a5 5 0 0 0-5 5c0 4 5 9 5 9s5-5 5-9a5 5 0 0 0-5-5zm0 7a2 2 0 1 1 0-4 2 2 0 0 1 0 4z" fill="#fff"/></svg>
      Beacon House, Port Alder, Grand Isle, Marlin Islands, Caribbean
    </span>
    <span>
      <svg width="14" height="10" viewBox="0 0 14 10"><rect x=".5" y=".5" width="13" height="9" fill="none" stroke="#fff"/><path d="M.5.5 7 6 13.5.5" fill="none" stroke="#fff"/></svg>
      info@42k17t.ky
    </span>
  </div>
  <div class="brand"><span class="brand-dot"></span><span class="brand-name">42K17T SEZC</span></div>
  <nav class="nav">
    <a href="#about">About Us</a>
    <a href="#contact">Contact Us</a>
    <a href="#timeline">Product Timeline</a>
    <span class="lang">ENG
      <svg width="10" height="6" viewBox="0 0 10 6"><path d="M0 0l5 6 5-6z" fill="#fff"/></svg>
    </span>
  </nav>
  <div class="hero-title">
    <h1>42K17T</h1>
    <div class="sezc">SEZC</div>
    <div class="tagline">Where Games Are Reimagined</div>
  </div>
</header>

<section class="about" id="about">
  <h2>About Us</h2>
  <p>Get ready to embark on an exhilarating journey with 42K17T SEZC, a dynamic, multi-platform game development company born in the heart of the Caribbean! Our diverse team hails from around the world, blending talent with passion. From fresh graduates to industry veterans, we've united under one vision: to radically reimagine existing games.</p>
  <p>With our debut title "Lumo," a captivating Colouring/Shade By Tile game for NovaOS, Droidline, DeskOS, and PC, we're set to showcase what true innovation looks like. Stay tuned to see how we're reshaping the gaming landscape, one Pixel at a time!</p>
</section>

<div class="product-badge"><div>Lumo</div></div>

<h2 class="timeline-title" id="timeline">Lumo Timeline</h2>
<div class="timeline-line"></div>

<div class="milestone" style="left:168px">
  <div class="label above">Lumo<br>Conceived</div>
  <div class="tick" style="top:1608px;height:14px"></div>
  <div class="dot blue">Q1-23</div>
</div>
<div class="milestone" style="left:324px">
  <div class="dot green">Q3-23</div>
  <div class="label below">Proof of<br>Concept</div>
</div>
<div class="milestone" style="left:484px">
  <div class="label above">Working Game<br>(PC Only)</div>
  <div class="dot blue">Q1-24</div>
</div>
<div class="milestone" style="left:640px">
  <div class="dot green">Q2-24</div>
  <div class="label below">Team Gathering<br>&amp; Pitch</div>
</div>
<div class="milestone" style="left:796px">
  <div class="label above">42K17T<br>Established</div>
  <div class="dot blue">Q3-24</div>
</div>
<div class="milestone" style="left:952px">
  <div class="dot green">Q4-24</div>
  <div class="label below">Lumo<br>Completed</div>
</div>
<div class="milestone" style="left:1108px">
  <div class="label above">Lumo Launched!</div>
  <div class="dot blue">Q1-25</div>
</div>

<section class="contact" id="contact" role="img" aria-label="Misty jungle coastline background">
  <h2>Contact Us</h2>
  <p class="by">by emailing <strong>info@42k17t.ky</strong></p>
  <a class="btn">EMAIL US
    <svg width="14" height="10" viewBox="0 0 14 10"><path d="M0 5h12M8 1l4 4-4 4" fill="none" stroke="#fff" stroke-width="1.5"/></svg>
  </a>
</section>

<div class="device">
  <div class="screen" role="img" aria-label="In-progress game screenshot: colouring canvas with a numbered palette column"></div>
</div>

<footer class="footer">Copyright © 2024 42K17T SEZC . All Right Reserved</footer>

</body>
</html>
```